practical mindfulness guide needs a book cover, back and front

I require a book cover for a print and eBook. Both front and back. The title of the book is: Returning to Stillness:
Refreshing Your Routine to Ease Worry, Grow Inner Awareness, and Open Your Boundless Promise.
Sales Handle
Eight weeks is good, fifty-two is better: this warm, personal guide will help you deepen in mindfulness across the year, weaving it into all aspects of your life.

Back cover
Returning to Stillness offers an evidence-based, step-by-step journey through a year of personal change. Drawing on his path of overcoming dyslexia, autism, trauma, and anxiety, Dr. Martin Olund blends mindfulness, psychology, and holistic healing in this accessible guide to lasting personal transformation.

Unlike short-term programs, this book offers a full year of structured, practical exercises—scientifically grounded and deeply personal—to help you turn mindfulness into a lifelong habit. Each week, you'll explore simple yet profound practices to manage stress, build emotional resilience, and reconnect with your deeper wisdom. Through guided meditations, reflections, and trainings, you’ll rewire old patterns and learn to embrace the present moment with clarity and compassion. Whether you're seeking relief from chronic stress, clarity in uncertain times, or a deeper connection to yourself and your life, Gentle Renewal will meet you where you are. It’s not about perfection—it’s about learning to show up, fully present, for the beauty and messiness of life.

Bio
Martin Olund is a mindfulness and Dharma teacher, award-winning author, and former professor of social work with over 40 years of contemplative practice. He teaches insight meditation and has worked extensively with diverse communities, including unhoused populations, combat veterans with PTSD, and First Nations groups, blending mindfulness with deep cultural respect. Martin holds a PhD in social work and has authored several mindfulness and social justice books. He teaches with Quiet Harbor Sangha (QHS) and founded the Cedarline Stillness Sitting Circle. His teaching invites a return to presence, clarity, and compassionate action.

I like the simple design of the book Awareness: The Quiet Secret Within Breathing and Living Fully in Your Days. But something more eye-catching would be welcome. It is a book for someone who has taken an intro mindfulness course and wants to get back into it, hence the "coming back" in the title. AI suggested things like a calendar with "practice" written on one day, with it crossed out. At any rate, it would be nice to illustrate this idea of coming back or renewing mindfulness practice with a 52-week practice guide. The book is basically 52 topics with an intro, reflections, practices, and encouragement.

Target Market(s)

Someone who has completed a short introductory mindfulness program like MBSR or MBCT and aims to cultivate a consistent, sustainable meditation and mindfulness practice. Eight weeks is a great start, but it simply isn’t enough time to firmly establish the habits of mindfulness, much less to delve into the layers of somatic and emotional nuance that it can offer. People require varying support levels. For example, those with chronic depression may need intensive follow-ups, while others might benefit from occasional refreshers. This book offers a flexible approach that readers can tailor to their own needs. The secondary target audience includes individuals who had a previous meditation practice but have let it lapse and wish to revitalize it. Through positive reviews, press, social media, and word-of-mouth, I also hope to attract other types of readers, such as those experiencing high stress or anxiety, individuals navigating major life transitions, professionals like therapists, counselors, and coaches, people seeking to develop resiliency or emotional intelligence, and those curious about integrating spiritual wisdom into everyday life.

Industry/Entity Type

Self help

Colors
0054AA
0677BA
7BADD7
CADEEF
E8F1F8

Requirements
Must have
• The title and my name as Martin J. Olund. Provided logo on bottom of back cover
Nice to have
• Something that says this book is for those coming back to practice. some tie in with my Youtube channel at https://www.videoplace.example/@martinsits
Should not have
• Buddhas or other religious symbols

```html
<!DOCTYPE html>
<html lang="en">
<head>
<meta charset="utf-8">
<title>Returning to Stillness — Front Cover</title>
<link href="https://fonts.googleapis.com/css2?family=Poppins:wght@300;400;700;800&display=swap" rel="stylesheet">
<style>
  :root {
    --stage-grey: #b3b3b3;
    --paper: #ffffff;
    --sky-blue: #4a89dc;
    --deep-navy: #0a4a86;
    --ink: #2b2b2b;
    --photo-light: #f4f6f8;
    --photo-mid: #e3e7eb;
  }
  html, body {
    margin: 0;
    padding: 0;
    width: 1200px;
    height: 1200px;
    overflow: hidden;
    background: var(--stage-grey);
  }
  .canvas {
    position: relative;
    width: 1200px;
    height: 1200px;
  }
  .front-cover {
    position: absolute;
    left: 291px;
    top: 160px;
    width: 618px;
    height: 880px;
    background: var(--paper);
    overflow: hidden;
    font-family: "Poppins", sans-serif;
  }
  .cover-art {
    position: absolute;
    inset: 0;
    width: 618px;
    height: 880px;
  }
  .title-block {
    position: absolute;
    left: 0;
    right: 0;
    top: 30px;
    text-align: center;
  }
  .title-lead {
    margin: 0;
    font-weight: 300;
    font-size: 50px;
    line-height: 1;
    letter-spacing: 1px;
    color: var(--sky-blue);
  }
  .title-main {
    margin: 4px 0 0;
    font-weight: 800;
    font-size: 62px;
    line-height: 1;
    letter-spacing: 2px;
    color: var(--deep-navy);
  }
  .subtitle {
    margin: 12px 0 0;
    font-weight: 400;
    font-size: 17.5px;
    line-height: 26px;
    color: var(--sky-blue);
  }
  .author-name {
    position: absolute;
    right: 36px;
    bottom: 18px;
    margin: 0;
    font-weight: 700;
    font-size: 25px;
    color: var(--ink);
  }
</style>
</head>
<body>
<div class="canvas">
  <section class="front-cover">
    <svg class="cover-art" viewBox="0 0 618 880" xmlns="http://www.w3.org/2000/svg">
      <defs>
        <radialGradient id="calendar-tone" cx="50%" cy="45%" r="60%">
          <stop offset="0%" stop-color="var(--photo-light)"/>
          <stop offset="100%" stop-color="var(--photo-mid)"/>
        </radialGradient>
      </defs>
      <!-- lower-left navy block -->
      <rect class="navy-block" x="0" y="522" width="309" height="358" fill="var(--deep-navy)"/>
      <!-- white sweep inside navy block -->
      <circle class="white-sweep" cx="310" cy="542" r="288" fill="var(--paper)"/>
      <!-- upper-left quarter band -->
      <path class="upper-band" d="M 23 522 A 288 288 0 0 1 291 254 L 291 522 Z" fill="var(--sky-blue)"/>
      <!-- lower-right quarter sweep -->
      <path class="lower-sweep" d="M 310 528 L 618 528 L 618 560 A 308 308 0 0 1 310 840 Z" fill="var(--sky-blue)"/>
      <!-- ring around the image -->
      <circle class="image-ring" cx="310" cy="542" r="250" fill="var(--sky-blue)"/>
      <!-- calendar photo area -->
      <circle class="calendar-photo" cx="310" cy="542" r="208" fill="url(#calendar-tone)"
              role="img" aria-label="Photo of a wall calendar with a red pushpin on one day and the word Practice handwritten beneath it"/>
    </svg>

    <header class="title-block">
      <h1 class="title-lead">RETURNING TO</h1>
      <h2 class="title-main">STILLNESS</h2>
      <p class="subtitle">Refreshing Your Routine to Ease Worry,<br>Grow Inner Awareness,<br>and Open Your Boundless Promise.</p>
    </header>

    <p class="author-name">Martin J. Olund</p>
  </section>
</div>
</body>
</html>
```